Hair Extension Packaging

Update 2/16 - please keep submissions coming, I have no front runners yet. Thanks.

I need some new packaging designed for hair extensions. I have enclose pictures of what other companies packaging looks like and a few pictures of some inspiration. I am looking for a packaging that will appeal to a 20's-30's year old demographic and I like things along the lines of glamor/lace/vintage/boudoir/damask inspired. I am going to leave colors up to your creativity for the sample artwork and ask for changes if needed. Id like the design to be a standout but not loud.

The working name for this hair is "Vexa"
Additional Text that I would like on the packaging "100% Premium Virgin Remy Human Hair"

Please keep in mind that the background of the packaging will have many different colors laying over it so be mindful of what the color you chose can effect the hair color in the packaging - no red or orange which can make the hair appear very warm and clash with ashy colors.

Working dimensions for the sample are 22" long, 3" wide.

****Once I decide on the front of the packaging I will also need the back designed which will consist of similar design as the front but with hair care instructions printed on it.***** This finished product must include front and back artwork, open Photoshop files, and additional bleed room for printing. I don't want to waste anyone's time so once I get a front design I like I will work with that artist to create the back.

Please message me with any questions.
Updates

Project Deadline Extended
Reason: Finalizing final choices. Thanks for your submissions!

Target Market(s)

Women in there 20"s - 30's. High fashion, luxurious, glamour

Industry/Entity Type

Hair

Font styles to use
Serif
Script

Requirements
Must have
• Id love the product name to be in script and then mixed with regular font (see the makeup logo example I enclosed)
Should not have
• Should not be masculine. Forget the blue and green colors

```html
<!DOCTYPE html>
<html lang="en">
<head>
<meta charset="utf-8">
<title>Vexa – Hair Extension Packaging Front</title>
<link rel="stylesheet" href="https://fonts.googleapis.com/css2?family=Great+Vibes&display=swap">
<style>
  :root {
    --paper: #ffffff;
    --blush-light: #f7ebe8;
    --blush: #ead0cb;
    --blush-deep: #dcb6b1;
    --ink: #1d1a0f;
    --band-espresso: #3e2a22;
    --band-text: #f4e8e2;
    --mauve: #a87c86;
    --mauve-mid: #cfaeb4;
  }
  html, body {
    margin: 0;
    padding: 0;
    width: 1200px;
    height: 3359px;
    overflow: hidden;
    background: var(--paper);
  }
  .package-front {
    position: relative;
    width: 1200px;
    height: 3359px;
    overflow: hidden;
    background: var(--paper);
  }
  .hair-wave-texture {
    position: absolute;
    left: 0;
    top: 0;
    width: 1200px;
    height: 2130px;
  }
  .brand-name {
    position: absolute;
    left: 0;
    top: 70px;
    width: 1200px;
    margin: 0;
    text-align: center;
    font-family: "Great Vibes", cursive;
    font-weight: 400;
    font-size: 330px;
    line-height: 380px;
    color: var(--ink);
  }
  .claim-band {
    position: absolute;
    left: 28px;
    top: 492px;
    width: 1112px;
    height: 66px;
    margin: 0;
    background: var(--band-espresso);
    color: var(--band-text);
    font-family: "Great Vibes", cursive;
    font-size: 50px;
    line-height: 68px;
    text-align: center;
    white-space: nowrap;
  }
  .colour-panel {
    position: absolute;
    left: 8px;
    top: 2066px;
    width: 1158px;
    height: 1272px;
    background: linear-gradient(180deg, var(--mauve) 0%, var(--mauve-mid) 40%, var(--paper) 100%);
  }
</style>
</head>
<body>
  <main class="package-front">
    <svg class="hair-wave-texture" viewBox="0 0 1200 2130" role="img" aria-label="Decorative pattern of fine wavy blush lines suggesting flowing hair">
      <defs>
        <linearGradient id="wave-fill" x1="0" y1="0" x2="1" y2="0">
          <stop offset="0" stop-color="var(--blush-light)"/>
          <stop offset="0.5" stop-color="var(--blush-deep)"/>
          <stop offset="1" stop-color="var(--blush-light)"/>
        </linearGradient>
      </defs>
      <path fill="url(#wave-fill)" d="M30 0 q-60 75 0 150 t0 150 t0 150 t0 150 t0 150 t0 150 t0 150 t0 150 t0 150 t0 150 t0 150 t0 150 t0 150 t0 150 L30 2130 L1170 2130 L1170 2100 q60 -75 0 -150 t0 -150 t0 -150 t0 -150 t0 -150 t0 -150 t0 -150 t0 -150 t0 -150 t0 -150 t0 -150 t0 -150 t0 -150 t0 -150 L1170 0 Z"/>
    </svg>
    <h1 class="brand-name">Vexa</h1>
    <p class="claim-band">100% Premium Virgin Remy Human Hair</p>
    <div class="colour-panel"></div>
  </main>
</body>
</html>
```